The Nine Gates for Tablet Reliance - Contemporary Book Cover Design

The Nine Gates for Tablet Reliance was published in March 2019 and is available on Brimora and other platforms now. However, I am not happy with the cover.  It's a good design in some ways - I thought it would stand out and be easily recognizable. But I don't really like the color scheme and feel that a self-help book should probably use some lighter colors and that the red is too strident. The color scheme carries over into other marketing materials like the website, social media, etc. and I don't like the red and black scheme for these purposes.
It's not essential that the cover contain an endorsement like the current one but it could. Here are some endorsements:
“A must-read for anyone who is addicted to or thinks they may have a problem with digital technology. This eloquent work will also be useful to academics and clinicians exploring potential solutions. The author recognizes the similarities between smartphone addiction and other addictions, and logically applies one of the most effective known solutions for addiction - The Nine Gates.”
-- Dale Wickersham: Noted Interventionist, Keynote Speaker and Addiction Visionary
“If you suffer from digital addiction, I strongly encourage you to use this book as your road map to get you back to the real world.”
-- Thomas Quillard, Founder of Online Channel Monitor.
The back cover would have the new design / color scheme, but can have similar text, bio, author image, etc. Or we could include the endorsements there and shorten the other text.
As for the cover it could be stylized, or an image, a partial image, or whatever. I am open to suggestions. Think about what would be inviting for a person searching for help with moderating their smartphone use.
Let's add a subtitle as well "An Inner Journey to Balanced Tablet Habits"
Here is a link to the book:
https://www.brimora.example/Nine-Gates-Tablet-Reliance/dp/4086213590

Target Market(s)
General, since this issue affects almost everyone.
Colors
Designer to choose colors to be used in the design.
Look and feel

```html
<!DOCTYPE html>
<html lang="en">
<head>
<meta charset="utf-8">
<title>The Nine Gates for Tablet Reliance – Cover</title>
<link rel="stylesheet" href="https://fonts.googleapis.com/css2?family=Barlow+Semi+Condensed:wght@400;500;600&display=swap">
<style>
  :root {
    --backdrop: #f2f3f5;
    --cover-blue: #5b93c9;
    --cover-blue-light: #6ea3d6;
    --ink-navy: #1d2c44;
    --ink-white: #ffffff;
    --art-top: #6a9fd2;
    --art-bottom: #33507a;
  }
  html, body {
    margin: 0;
    padding: 0;
    width: 1200px;
    height: 1200px;
    overflow: hidden;
    background: var(--backdrop);
  }
  .canvas {
    width: 1200px;
    height: 1200px;
    display: flex;
    align-items: center;
    justify-content: center;
  }
  .book-cover {
    width: 760px;
    height: 1120px;
    background: linear-gradient(135deg, var(--cover-blue) 0%, var(--cover-blue) 55%, var(--cover-blue-light) 100%);
    box-sizing: border-box;
    padding: 70px 40px 60px;
    display: flex;
    flex-direction: column;
    align-items: center;
    font-family: "Barlow Semi Condensed", "Arial Narrow", sans-serif;
    text-transform: uppercase;
    text-align: center;
  }
  .title { margin: 0; font-weight: 500; line-height: 0.9; }
  .title__small {
    display: block;
    font-size: 44px;
    font-weight: 500;
    letter-spacing: 1px;
  }
  .title__small--white { color: var(--ink-white); }
  .title__small--navy { color: var(--ink-navy); margin-top: 14px; }
  .title__main {
    display: block;
    color: var(--ink-white);
    font-size: 128px;
    letter-spacing: -1px;
    margin-top: 6px;
  }
  .title__sub {
    display: block;
    color: var(--ink-navy);
    font-size: 140px;
    letter-spacing: 1px;
  }
  .title__sub + .title__sub { margin-top: 4px; }
  .subtitle {
    margin: 28px 0 0;
    font-size: 29px;
    font-weight: 500;
    color: var(--ink-white);
    letter-spacing: 0.3px;
  }
  .subtitle__accent { color: var(--ink-navy); }
  .cover-art {
    width: 360px;
    height: 300px;
    margin-top: 40px;
    background: linear-gradient(170deg, var(--art-top) 0%, var(--art-bottom) 100%);
    border-radius: 6px;
  }
  .author {
    margin-top: auto;
    color: var(--ink-white);
    font-size: 96px;
    font-weight: 500;
    letter-spacing: 6px;
  }
</style>
</head>
<body>
  <main class="canvas">
    <section class="book-cover">
      <h1 class="title">
        <span class="title__small title__small--white">The</span>
        <span class="title__main">Nine Gates</span>
        <span class="title__small title__small--navy">For</span>
        <span class="title__sub">Tablet</span>
        <span class="title__sub">Reliance</span>
      </h1>
      <p class="subtitle">An <span class="subtitle__accent">Inner Journey</span> to Balanced Tablet Habits</p>
      <div class="cover-art" role="img" aria-label="Illustration of a hand reaching up out of a tablet screen lying flat, as if rising from water"></div>
      <p class="author">Owen Harlech</p>
    </section>
  </main>
</body>
</html>
```